DOG DAYCARE BILLBOARD

Design a bold exciting billboard that can be read easily from a distance! Our goal is brand awareness and showcasing the services we offer (Boarding, Grooming, Daycare, and Training.
we would like to see examples with the phrase "your best friend's best day". Our name Bright Meadow Canine Activity Center (or just Bright Meadow might work better and could be bigger) and the services we provide.
(there are two examples of what we like included in the pictures)
you can find more information o our website at pawplayhouse@mailbox-example.com.

```html
<!DOCTYPE html>
<html lang="en">
<head>
<meta charset="utf-8">
<title>Bright Meadow Billboard</title>
<link href="https://fonts.googleapis.com/css2?family=Michroma&display=swap" rel="stylesheet">
<style>
  :root {
    --page-bg: #ffffff;
    --panel-bg: #f7f7f7;
    --panel-edge: #e4e4e4;
    --ink: #1a1a1a;
    --orange: #e2720b;
    --band-text: #ffffff;
    --photo-light: #f2ede8;
    --photo-warm: #c9772f;
    --photo-deep: #a4561b;
  }
  * { margin: 0; padding: 0; box-sizing: border-box; }
  html, body {
    width: 1140px;
    height: 1200px;
    overflow: hidden;
    background: var(--page-bg);
  }
  .billboard {
    position: absolute;
    left: 40px;
    top: 343px;
    width: 1060px;
    height: 514px;
    background: linear-gradient(180deg, #ffffff 0%, var(--panel-bg) 100%);
    border: 1px solid var(--panel-edge);
    font-family: "Michroma", sans-serif;
    color: var(--ink);
    overflow: hidden;
  }
  .dog-photo {
    position: absolute;
    left: 0;
    top: 30px;
    width: 285px;
    height: 386px;
    background:
      radial-gradient(ellipse 60% 45% at 48% 30%, var(--photo-warm) 0%, rgba(201,119,47,0.85) 55%, rgba(201,119,47,0) 100%),
      radial-gradient(ellipse 70% 60% at 40% 85%, var(--photo-deep) 0%, rgba(164,86,27,0.8) 60%, rgba(164,86,27,0) 100%),
      linear-gradient(180deg, var(--photo-light), #e9ddd2);
  }
  .brand {
    position: absolute;
    left: 380px;
    top: 60px;
    width: 510px;
    display: flex;
    flex-direction: column;
    align-items: center;
    gap: 14px;
  }
  .brand-mark {
    width: 92px;
    height: 92px;
    border-radius: 50%;
    background: var(--ink);
  }
  .brand-name {
    font-size: 30px;
    letter-spacing: 1px;
    color: var(--ink);
    text-align: center;
    line-height: 1.25;
  }
  .brand-name small {
    display: block;
    font-size: 13px;
    letter-spacing: 2px;
  }
  .headline {
    position: absolute;
    left: 290px;
    right: 20px;
    top: 255px;
    text-align: center;
    line-height: 1;
  }
  .headline-top {
    display: block;
    font-size: 46px;
    color: var(--ink);
    -webkit-text-stroke: 1px var(--ink);
  }
  .headline-main {
    display: block;
    margin-top: 6px;
    font-size: 90px;
    color: var(--orange);
    -webkit-text-stroke: 2px var(--orange);
  }
  .services {
    position: absolute;
    left: 0;
    right: 0;
    top: 416px;
    height: 84px;
    background: var(--orange);
    display: flex;
    justify-content: space-evenly;
    align-items: center;
    list-style: none;
  }
  .services li {
    display: flex;
    align-items: center;
    gap: 10px;
    font-size: 29px;
    color: var(--band-text);
    -webkit-text-stroke: 0.6px var(--band-text);
  }
  .services li::before {
    content: "";
    width: 14px;
    height: 14px;
    border-radius: 50%;
    background: var(--band-text);
  }
</style>
</head>
<body>
  <section class="billboard">
    <div class="dog-photo" role="img" aria-label="Photo of a golden-red dog sitting and holding a grey striped plush toy in its mouth"></div>

    <div class="brand">
      <span class="brand-mark"></span>
      <p class="brand-name">BRIGHT MEADOW<small>CANINE ACTIVITY CENTER LLC</small></p>
    </div>

    <h1 class="headline">
      <span class="headline-top">YOUR BEST FRIEND'S</span>
      <span class="headline-main">BEST DAY!</span>
    </h1>

    <ul class="services">
      <li>BOARDING</li>
      <li>DAYCARE</li>
      <li>GROOMING</li>
      <li>TRAINING</li>
    </ul>
  </section>
</body>
</html>
```